Simple, Professional and neat business card design for Vendralo Inc.

We're looking to re-vamp our business card design. We're a supplier of innovative feed ingredients for the North American animal agriculture industry. We are located in Lucknow, Ontario, Canada and our flagship product is a product that prevents milk fever in dairy cows when the calve, it is fed before calving and is very effective compared to other alternatives available on the market today.

Our company has Danish roots and we import all of our product from our Danish partner/manufacturer in Denmark. We like our design to embrace high professionalism while remaining neat and simple.

Target Market(s)

B2B, Feed Mills, Veterinary Clinics, Large integrators/producers,

Industry/Entity Type

Agribusiness

Contact Information for Business Card

We like the rounded corners because they make the card easy to sit in a wallet and not many use it so it makes the card stand out, just possibly something to take account for during the design.

As you can also see on the sliders below, looking for a that simple but proffesional scandinavian design.

Requirements
Nice to have
• Rounded corners
Should not have
• Too vibrant

```html
<!DOCTYPE html>
<html lang="en">
<head>
<meta charset="utf-8">
<title>Vendralo Inc. – Business Card</title>
<link href="https://fonts.googleapis.com/css2?family=Lato:wght@400;700;900&display=swap" rel="stylesheet">
<style>
  :root {
    --navy: #1c4e94;
    --navy-dark: #173f7a;
    --gold: #c9a96a;
    --gold-light: #f1e3c2;
    --card: #ffffff;
    --backdrop: #e4e6ea;
    --shadow: rgba(20, 30, 50, 0.18);
  }
  * { margin: 0; padding: 0; box-sizing: border-box; }
  html, body {
    width: 1200px; height: 900px; overflow: hidden;
    background: var(--backdrop);
    font-family: "Lato", Arial, sans-serif;
    color: var(--navy);
  }
  .stage { position: relative; width: 1200px; height: 900px; }
  .card {
    position: absolute;
    width: 600px; height: 343px;
    background: var(--card);
    border-radius: 26px;
    box-shadow: 0 14px 34px var(--shadow);
  }
  .card--back { left: 300px; top: 70px; }
  .back-mark {
    position: absolute; left: 0; right: 0; top: 120px;
    display: flex; align-items: center; justify-content: center; gap: 10px;
  }
  .mark-square { width: 22px; height: 22px; background: var(--navy); border-radius: 3px; }
  .mark-name { font-weight: 900; font-size: 26px; color: var(--navy); }
  .back-web {
    position: absolute; left: 0; right: 0; top: 190px;
    text-align: center; font-size: 15px; color: var(--navy);
  }
  .back-web strong { font-weight: 900; }

  .card--front { left: 300px; top: 470px; }
  .logo-slot {
    position: absolute; left: 38px; top: 78px;
    width: 96px; height: 96px; border-radius: 50%;
    background: radial-gradient(circle at 50% 40%, var(--gold-light), var(--gold));
    border: 5px solid var(--navy);
  }
  .social {
    position: absolute; right: 34px; top: 30px;
    font-size: 12px; font-weight: 700; color: var(--navy);
  }
  .company {
    position: absolute; left: 156px; top: 72px;
    font-weight: 900; font-size: 50px; letter-spacing: 0.5px;
    color: var(--navy); line-height: 1;
  }
  .address {
    position: absolute; left: 160px; top: 130px;
    font-size: 16px; color: var(--navy);
  }
  .phones {
    position: absolute; right: 34px; top: 184px;
    display: grid; grid-template-columns: auto auto;
    column-gap: 8px; row-gap: 1px; align-items: baseline;
  }
  .phones dt {
    text-align: right; font-size: 9px; font-weight: 700;
    letter-spacing: 0.8px; text-transform: uppercase; color: var(--navy-dark);
  }
  .phones dd { font-size: 17px; color: var(--navy); letter-spacing: 0.5px; }
  .person { position: absolute; left: 40px; top: 230px; }
  .person-name { font-weight: 900; font-size: 17px; text-transform: uppercase; }
  .person-role { font-weight: 700; font-size: 13px; }
  .email { position: absolute; left: 40px; top: 290px; font-size: 16px; }
</style>
</head>
<body>
<main class="stage">
  <section class="card card--back" aria-label="Card back">
    <div class="back-mark">
      <span class="mark-square"></span>
      <span class="mark-name">Vendralo</span>
    </div>
    <p class="back-web">www.<strong>vendralo</strong>.com</p>
  </section>

  <section class="card card--front" aria-label="Card front">
    <div class="logo-slot" role="img" aria-label="Company emblem"></div>
    <p class="social">@vendralo</p>
    <h1 class="company">VENDRALO INC.</h1>
    <p class="address">212 Harbour Road, Elmbrook, Northvale</p>
    <dl class="phones">
      <dt>Mobile</dt><dd>555 010 0141</dd>
      <dt>Office</dt><dd>555 010 0172</dd>
      <dt>Toll free</dt><dd>555 010 0193</dd>
      <dt>Fax</dt><dd>555 010 0188</dd>
    </dl>
    <div class="person">
      <p class="person-name">Mikkel Sorensen</p>
      <p class="person-role">managing director</p>
    </div>
    <p class="email">mikkel@vendralo.com</p>
  </section>
</main>
</body>
</html>
```